Rig up a website for a Rigging Company

We already have a logo. Looking for a website design that works on plivano.com.
Our rigging company uses semi trucks, forklifts, and similar equipment to move large machines.
Our logo is white, black and red.

Target Market(s)

Medical Industry (moving medical equipment), Utility Industry (power equipment), Food Industry (moving bottling/packing equipment), US Government (large equipment)

Industry/Entity Type

It Company

Coding

Coded - Design and coding required

Number of Pages Required

5+ page

Font styles to use
Sans Serif

Colors
ec1f27
ffffff
0355a3

Requirements
Must have
• Home page, About page, Services Page, and Contact Information page
Nice to have
• Pictures of semi and forklifts and ability to insert our own pictures of our equipment

```html
<!DOCTYPE html>
<html lang="en">
<head>
<meta charset="utf-8">
<title>Halvern Rigging</title>
<link href="https://fonts.googleapis.com/css2?family=Mulish:wght@400;600;700&family=Open+Sans:wght@400;600&family=Raleway:wght@500;600&display=swap" rel="stylesheet">
<style>
  :root {
    --red: #e01e26;
    --red-dark: #a8141a;
    --ink: #2b2b2b;
    --muted: #7a7a7a;
    --grey-bg: #efefef;
    --card-line: #d9d9d9;
    --footer: #222222;
    --footer-bottom: #1a1a1a;
    --white: #ffffff;
    --title-blue: #2f3f55;
  }
  * { margin: 0; padding: 0; box-sizing: border-box; }
  html, body { width: 1200px; height: 2439px; overflow: hidden; }
  body { position: relative; background: var(--white); font-family: "Open Sans", sans-serif; color: var(--ink); }
  .abs { position: absolute; }

  /* Header */
  .site-header { position: absolute; left: 0; top: 0; width: 1200px; height: 109px; background: var(--white); }
  .brand { position: absolute; left: 117px; top: 28px; display: flex; align-items: center; gap: 12px; }
  .brand-mark { width: 22px; height: 22px; background: var(--red); }
  .brand-name { font-family: "Mulish", sans-serif; font-weight: 700; font-size: 34px; color: #111; letter-spacing: 0.5px; }
  .main-nav a { position: absolute; top: 42px; font-family: "Mulish", sans-serif; font-size: 17px; color: #333; text-decoration: none; letter-spacing: 0.3px; }
  .main-nav a.active { color: var(--red); }
  .nav-underline { position: absolute; left: 428px; top: 104px; width: 65px; height: 5px; background: var(--red); }

  /* Hero */
  .hero { position: absolute; left: 0; top: 109px; width: 1200px; height: 541px;
    background: linear-gradient(180deg, #4e4f78 0%, #8a7d9a 35%, #d9a877 62%, #5a4a4a 82%, #1f1c22 100%); }
  .hero-title { position: absolute; left: 111px; top: 222px; font-family: "Mulish", sans-serif; font-weight: 700; font-size: 42px; line-height: 46px; color: var(--white); text-transform: uppercase; letter-spacing: 0.5px; }
  .hero-dots { position: absolute; left: 117px; top: 348px; display: flex; gap: 10px; }
  .hero-dots span { width: 14px; height: 14px; border-radius: 50%; background: var(--white); border: 2px solid var(--white); }
  .hero-dots span.current { background: transparent; }

  /* About */
  .about { position: absolute; left: 0; top: 650px; width: 1200px; height: 410px; background: var(--white); overflow: hidden; }
  .about-photo { position: absolute; left: 0; top: 0; width: 1200px; height: 410px; }
  .about-title { position: absolute; left: 112px; top: 68px; font-family: "Mulish", sans-serif; font-weight: 600; font-size: 34px; color: #222; }
  .about-text { position: absolute; left: 110px; font-size: 14.5px; line-height: 27.6px; color: #666; width: 470px; }
  .btn-dark { position: absolute; left: 110px; top: 300px; width: 137px; height: 37px; border-radius: 3px; background: linear-gradient(#6a6a6a, #444); color: var(--white); font-family: "Raleway", sans-serif; font-weight: 600; font-size: 13px; display: flex; align-items: center; justify-content: center; }

  /* Services */
  .services { position: absolute; left: 0; top: 1060px; width: 1200px; height: 555px; background: var(--grey-bg); }
  .section-heading { position: absolute; left: 0; top: 40px; width: 1200px; display: flex; justify-content: center; align-items: center; gap: 16px; font-family: "Mulish", sans-serif; font-weight: 600; font-size: 29px; color: #444; }
  .section-heading::before, .section-heading::after { content: ""; width: 38px; height: 1px; background: #888; }
  .service-card { position: absolute; top: 109px; width: 315px; height: 395px; background: var(--white); border: 1px solid var(--card-line); }
  .service-photo { width: 100%; height: 194px; }
  .service-title { position: absolute; left: 29px; top: 224px; font-family: "Open Sans", sans-serif; font-size: 24px; color: var(--red-dark); }
  .service-text { position: absolute; left: 29px; top: 266px; width: 260px; font-size: 13.3px; line-height: 19.5px; color: #8a8a8a; }
  .btn-outline { position: absolute; left: 29px; top: 334px; width: 110px; height: 34px; border: 2px solid var(--red); color: var(--red-dark); font-family: "Raleway", sans-serif; font-weight: 500; font-size: 13px; display: flex; align-items: center; justify-content: center; }

  /* Projects */
  .projects-heading { position: absolute; left: 114px; top: 1694px; font-family: "Mulish", sans-serif; font-weight: 700; font-size: 26px; color: #333; }
  .project { position: absolute; top: 1748px; }
  .project-photo { position: absolute; left: 0; top: 0; width: 236px; height: 179px; }
  .project-title { position: absolute; left: 257px; top: 2px; white-space: nowrap; font-family: "Open Sans", sans-serif; font-size: 19px; color: var(--title-blue); }
  .project-text { position: absolute; left: 257px; top: 42px; width: 215px; font-size: 14.3px; line-height: 22px; color: #777; }
  .project-link { position: absolute; left: 257px; top: 160px; white-space: nowrap; font-size: 15px; color: var(--red-dark); }

  /* Footer */
  .site-footer { position: absolute; left: 0; top: 2034px; width: 1200px; height: 333px; background: var(--footer); color: var(--white); }
  .footer-col { position: absolute; top: 63px; }
  .footer-col h3 { font-family: "Mulish", sans-serif; font-weight: 400; font-size: 20px; margin-bottom: 9px; text-transform: uppercase; }
  .footer-col li { list-style: none; font-size: 13.5px; line-height: 24.4px; color: #cfcfcf; }
  .contact-line { display: flex; align-items: flex-start; gap: 10px; font-size: 13.5px; line-height: 22px; color: #cfcfcf; }
  .contact-line svg { flex: none; margin-top: 4px; }
  .social { position: absolute; left: 522px; top: 225px; display: flex; gap: 10px; }
  .social span { width: 32px; height: 32px; border-radius: 50%; background: var(--red); }
  .footer-brand { position: absolute; left: 810px; top: 90px; display: flex; align-items: center; gap: 12px; }
  .footer-brand .brand-mark { background: var(--red); }
  .footer-brand .brand-name { color: var(--white); font-size: 38px; }
  .footer-bottom { position: absolute; left: 0; top: 2367px; width: 1200px; height: 72px; background: var(--footer-bottom); display: flex; align-items: center; justify-content: center; font-size: 12.5px; color: #aaa; padding-right: 6px; }
</style>
</head>
<body>

<header class="site-header">
  <div class="brand"><span class="brand-mark"></span><span class="brand-name">Halvern Rigging</span></div>
  <nav class="main-nav">
    <a class="active" style="left:436px">HOME</a>
    <a style="left:522px">ABOUT US</a>
    <a style="left:639px">SERVICES</a>
    <a style="left:750px">EQUIPMENT</a>
    <a style="left:889px">PROJECT</a>
    <a style="left:1006px">CONTACT</a>
  </nav>
  <div class="nav-underline"></div>
</header>

<section class="hero" role="img" aria-label="Construction cranes silhouetted against a sunset sky">
  <h1 class="hero-title">Fusce ultricies orci ac<br>feugiat suscipit</h1>
  <div class="hero-dots"><span class="current"></span><span></span><span></span><span></span></div>
</section>

<section class="about">
  <svg class="about-photo" width="1200" height="410" viewBox="0 0 1200 410" role="img" aria-label="Forklift moving equipment in a warehouse, red tinted">
    <defs>
      <linearGradient id="aboutRed" x1="0" y1="0" x2="1" y2="1">
        <stop offset="0" stop-color="#e3262b"/>
        <stop offset="0.6" stop-color="#c8151b"/>
        <stop offset="1" stop-color="#a30f14"/>
      </linearGradient>
    </defs>
    <polygon points="680,0 1200,0 1200,410 527,410" fill="url(#aboutRed)"/>
  </svg>
  <h2 class="about-title">About Halvern Rigging</h2>
  <p class="about-text" style="top:124px">Fusce ultricies orci ac feugiat suscipit leo massa sodales velit et scelerisque mi tortor at ipsum cligula augue</p>
  <p class="about-text" style="top:192px">bibendum accumsan vestibulum ut commodo a mi Morbi ornare gravida elit Integer congue augue et malesuada iaculis ipsum dui ali-quet felis at cursus magna nisl nec elit Praesent</p>
  <div class="btn-dark">READ MORE</div>
</section>

<section class="services">
  <h2 class="section-heading">What We Do</h2>

  <article class="service-card" style="left:110px">
    <div class="service-photo" role="img" aria-label="Semi truck on a highway" style="background:linear-gradient(180deg,#c9ced8 0%,#8f97a6 45%,#2e3342 75%,#6d6a66 100%)"></div>
    <h3 class="service-title">Semi Trucks</h3>
    <p class="service-text">Donec dictum lectus non odio Cras a ante vitae enim iaculis aliquam Mauris nunc quam venenatis nec euismod</p>
    <div class="btn-outline">Read More</div>
  </article>

  <article class="service-card" style="left:444px">
    <div class="service-photo" role="img" aria-label="Row of forklifts in a warehouse" style="background:linear-gradient(135deg,#3a3a3a 0%,#6b6b68 40%,#c9a82a 62%,#3d3d3d 100%)"></div>
    <h3 class="service-title">Forklifts</h3>
    <p class="service-text">Donec dictum lectus non odio Cras a ante vitae enim iaculis aliquam Mauris nunc quam venenatis nec euismod</p>
    <div class="btn-outline">Read More</div>
  </article>

  <article class="service-card" style="left:779px">
    <div class="service-photo" role="img" aria-label="Crane lifting a machine against a blue sky" style="background:linear-gradient(180deg,#1f6fd0 0%,#4b95e6 50%,#c8dcf2 100%)"></div>
    <h3 class="service-title">Move Machines</h3>
    <p class="service-text">Donec dictum lectus non odio Cras a ante vitae enim iaculis aliquam Mauris nunc quam venenatis nec euismod</p>
    <div class="btn-outline">Read More</div>
  </article>
</section>

<h2 class="projects-heading">RECENT PROJECTS</h2>

<article class="project" style="left:115px">
  <div class="project-photo" role="img" aria-label="Offshore drilling platform at sea" style="background:linear-gradient(180deg,#7fb0e0 0%,#c9722e 45%,#d85a1f 60%,#2b6f9a 100%)"></div>
  <h3 class="project-title">Project Tittle here</h3>
  <p class="project-text">tellus nec ultricies sit amet porttitor mattis enim In massa libero interdum nec interdum vel blandit sed nulla In ullamcorper est e</p>
  <span class="project-link">READ MORE</span>
</article>

<article class="project" style="left:621px">
  <div class="project-photo" role="img" aria-label="Mobile crane truck on a job site" style="background:linear-gradient(180deg,#2c4fb8 0%,#6b86c9 45%,#d8d8d6 70%,#4a4a4a 100%)"></div>
  <h3 class="project-title">Project Tittle here</h3>
  <p class="project-text">tellus nec ultricies sit amet porttitor mattis enim In massa libero interdum nec interdum vel blandit sed nulla In ullamcorper est e</p>
  <span class="project-link">READ MORE</span>
</article>

<footer class="site-footer">
  <div class="footer-col" style="left:115px">
    <h3>Company</h3>
    <ul><li>Home</li><li>About Us</li><li>Why Us</li><li>Our Services</li><li>Our Team</li></ul>
  </div>
  <div class="footer-col" style="left:320px">
    <h3>Resources</h3>
    <ul><li>Our Equipments</li><li>Our Projects</li><li>News</li><li>Blogs</li><li>Conact Us</li></ul>
  </div>
  <div class="footer-col" style="left:522px">
    <h3>Contact Us</h3>
    <div class="contact-line">
      <svg width="12" height="16" viewBox="0 0 12 16"><path d="M6 0a6 6 0 0 0-6 6c0 4.5 6 10 6 10s6-5.5 6-10a6 6 0 0 0-6-6zm0 8.5a2.5 2.5 0 1 1 0-5 2.5 2.5 0 0 1 0 5z" fill="#fff"/></svg>
      <span>412 Millbrook Lane Suite<br>210 Aldenford, Georgia 30190</span>
    </div>
    <div class="contact-line" style="margin-top:4px">
      <svg width="14" height="14" viewBox="0 0 14 14"><path d="M3 0l2.5 3.5-1.5 1.5c.8 1.8 2.2 3.2 4 4l1.5-1.5L13 10l-1.5 3C6 13 1 8 1 2.5z" fill="#fff"/></svg>
      <span>555-014-2297</span>
    </div>
    <div class="contact-line" style="margin-top:4px">
      <svg width="14" height="14" viewBox="0 0 14 14"><rect x="1" y="4" width="12" height="9" rx="1" fill="#fff"/><rect x="3" y="1" width="8" height="4" fill="#fff"/><rect x="3.5" y="7" width="7" height="1.4" fill="#222"/><rect x="3.5" y="9.5" width="7" height="1.4" fill="#222"/></svg>
      <span>555-018-6631</span>
    </div>
  </div>
  <div class="social" aria-label="Social links"><span></span><span></span><span></span><span></span></div>
  <div class="footer-brand"><span class="brand-mark"></span><span class="brand-name">Halvern Rigging</span></div>
</footer>

<div class="footer-bottom">© 2017 Company Name &nbsp;All right reserved &nbsp;Term of Use</div>

</body>
</html>
```